Innovative Healthcare Technology Company needs a Business Card Design

We are in need of an innovative business card design for a new healthcare software company called "Lumenwise Data Partners". We develop software that creates medical assessment applications and mobile e-learning prevention services to reduce risk behaviors in adolescent and young adults. Our initial product, the "KESTREL App", conducts a tailored sexual risk assessment and provides a doctor with an insightful patient report to improve sexual risk counseling and ultimately reduce unintended pregnancy, STDs, etc.

We would like the design to incorporate our logo and branding colors (attached) in an innovative and creative manner. The final design should communicate professionalism and healthcare innovation. Our tag line is "prevention is the solution" (doesn't necessarily need to be included) and our target audience is doctors, medical directors, and medical business administrators. Please visit our website for additional info ourbrightmarq.com. Be creative and we look forward to seeing your designs!

Target Market(s)

healthcare - doctors, medical directors and medical business administrators

Industry/Entity Type

Healthcare

Contact Information for Business Card

We would like the design to incorporate our logo and branding colors (attached) in an innovative and creative manner. The final design should communicate professionalism and healthcare innovation. Our tag line is "prevention is the solution" (doesn't necessarily need to be included)

Font styles to use
Other font styles liked:
• quicksand

Requirements
Must have
• our logo and brand colors
• Name, (Mara Feldhovenik, PhD)
• Email (drmara@ourbrightmarq.com)
• phone (555.283.9170)
• Website (ourbrightmarq.com)
Should not have
• cartoon look

```html
<!DOCTYPE html>
<html lang="en">
<head>
<meta charset="utf-8">
<title>Lumenwise Data Partners – Business Card</title>
<link rel="stylesheet" href="https://fonts.googleapis.com/css2?family=PT+Sans:wght@400&family=Quicksand:wght@400&display=swap">
<style>
  :root {
    --navy: #27557e;
    --sage: #7aa58e;
    --slate: #8a8c8f;
    --paper: #ffffff;
    --backdrop: #eeece8;
    --tile-light: #eef3f5;
    --tile-soft: #dfe7ea;
    --tile-white: #f7f8f8;
  }
  * { box-sizing: border-box; margin: 0; padding: 0; }
  html, body { width: 1200px; height: 1000px; overflow: hidden; }
  body { background: var(--backdrop); position: relative; font-family: "PT Sans", sans-serif; }

  .card {
    position: absolute;
    left: 226px;
    width: 747px;
    height: 428px;
    background: var(--paper);
    box-shadow: 0 2px 8px rgba(0,0,0,0.12);
  }
  .card--front { top: 55px; }
  .card--back { top: 517px; height: 427px; }

  /* Front mosaic */
  .tile { position: absolute; width: 135px; height: 124px; }
  .tile--navy { background: var(--navy); }
  .tile--sage { background: var(--sage); }
  .tile--photo-a { background: linear-gradient(135deg, var(--tile-soft), var(--tile-light)); }
  .tile--photo-b { background: linear-gradient(160deg, var(--tile-white), var(--tile-soft)); }
  .tile--photo-c { background: linear-gradient(200deg, #e8edf0, #f4f5f5); }

  .brand {
    position: absolute;
    display: flex;
    align-items: center;
    font-family: "Quicksand", sans-serif;
    font-weight: 400;
    color: var(--navy);
    white-space: nowrap;
  }
  .brand__square { background: var(--sage); flex: none; }
  .brand--front { left: 313px; top: 188px; font-size: 31px; gap: 14px; }
  .brand--front .brand__square { width: 26px; height: 26px; }
  .brand--back { left: 33px; top: 68px; font-size: 23px; gap: 11px; }
  .brand--back .brand__square { width: 20px; height: 20px; }

  /* Back */
  .person { position: absolute; right: 45px; top: 40px; text-align: right; color: var(--navy); }
  .person__name { font-size: 38px; line-height: 1.1; }
  .person__role { font-size: 19px; margin-top: 12px; }

  .contacts { position: absolute; left: 33px; top: 191px; list-style: none; }
  .contact { display: flex; align-items: center; height: 26px; margin-bottom: 10.5px; color: var(--navy); font-size: 22px; }
  .contact__icon { width: 26px; height: 26px; margin-right: 14px; flex: none; }

  .web-band {
    position: absolute; left: 0; top: 326px; width: 100%; height: 77px;
    background: var(--navy); color: var(--paper);
    display: flex; align-items: center; justify-content: center;
    font-size: 22px;
  }
</style>
</head>
<body>

<section class="card card--front" aria-label="Card front">
  <div class="tile tile--photo-a" style="left:21px;top:20px" role="img" aria-label="Photo crop: bright clinic window"></div>
  <div class="tile tile--navy" style="left:164px;top:20px"></div>
  <div class="tile tile--photo-b" style="left:307px;top:20px" role="img" aria-label="Photo crop: doctor's white coat and stethoscope"></div>
  <div class="tile tile--photo-b" style="left:450px;top:20px" role="img" aria-label="Photo crop: coat collar with stethoscope"></div>
  <div class="tile tile--photo-c" style="left:593px;top:20px" role="img" aria-label="Photo crop: blurred clinic background"></div>

  <div class="tile tile--photo-b" style="left:21px;top:153px" role="img" aria-label="Photo crop: hand over a tablet"></div>
  <div class="tile tile--photo-b" style="left:164px;top:153px" role="img" aria-label="Photo crop: stethoscope and tablet"></div>

  <div class="tile tile--photo-a" style="left:21px;top:284px" role="img" aria-label="Photo crop: coat sleeve"></div>
  <div class="tile tile--photo-c" style="left:164px;top:284px" role="img" aria-label="Photo crop: hand holding a tablet"></div>
  <div class="tile tile--photo-b" style="left:307px;top:284px" role="img" aria-label="Photo crop: white coat front"></div>
  <div class="tile tile--sage" style="left:450px;top:284px"></div>
  <div class="tile tile--photo-a" style="left:593px;top:284px" role="img" aria-label="Photo crop: clinic window light"></div>

  <div class="brand brand--front"><span class="brand__square"></span>Lumenwise Data Partners</div>
</section>

<section class="card card--back" aria-label="Card back">
  <div class="brand brand--back"><span class="brand__square"></span>Lumenwise Data Partners</div>

  <div class="person">
    <p class="person__name">Evan Tallow</p>
    <p class="person__role">Executive Manager</p>
  </div>

  <ul class="contacts">
    <li class="contact">
      <svg class="contact__icon" viewBox="0 0 26 26" aria-hidden="true">
        <rect width="26" height="26" rx="2" fill="var(--slate)"/>
        <path d="M9 6c1 0 2 2.5 2 3.3 0 .8-1.3 1.2-1.1 2 .5 1.7 2.3 3.8 4 4.6.8.3 1.3-1 2.1-1 .8 0 3 1.3 3 2.3 0 1.5-1.7 2.4-3 2.2C11 18.6 7 14 6.6 9.6 6.4 7.8 7.6 6 9 6z" fill="#fff"/>
      </svg>
      (00) 12 3456 7890
    </li>
    <li class="contact">
      <svg class="contact__icon" viewBox="0 0 26 26" aria-hidden="true">
        <rect width="26" height="26" rx="2" fill="var(--sage)"/>
        <rect x="8.5" y="5" width="9" height="16" rx="1.5" fill="none" stroke="#fff" stroke-width="1.6"/>
        <rect x="10.3" y="7.2" width="5.4" height="5" fill="#fff"/>
        <circle cx="13" cy="17.8" r="1.1" fill="#fff"/>
      </svg>
      (00) 12 3456 7890
    </li>
    <li class="contact">
      <svg class="contact__icon" viewBox="0 0 26 26" aria-hidden="true">
        <rect width="26" height="26" rx="2" fill="var(--navy)"/>
        <rect x="6" y="8" width="14" height="10" fill="#fff"/>
        <path d="M6 8l7 6 7-6" fill="none" stroke="var(--navy)" stroke-width="1.5"/>
      </svg>
      youremail@mail.com
    </li>
  </ul>

  <div class="web-band">www.lumenwisedata.com</div>
</section>

</body>
</html>
```